Hot Consulting firm collateral upgrade

We need a stationary design for our Oakland based consulting company called Tarvulix. We provide consulting expertise in BQR compliance for Medical Device, Pharmaceutical, and Biotech companies. We will be using the stationary for all of our marketing collateral. We want the design to convey professionalism and quality. You can find our company color scheme from our website tarvulix-hq.com. I have included a copy of our current stationary that needs an upgrade.
Target Market(s)
Medical Device, Pharma, and Biotech companies
Industry/Entity Type
It Company
Look and feel

```html
<!DOCTYPE html>
<html lang="en">
<head>
<meta charset="utf-8">
<title>Tarvulix Business Card</title>
<link rel="stylesheet" href="https://fonts.googleapis.com/css2?family=Source+Sans+3:wght@400;600;700&display=swap">
<style>
  :root {
    --backdrop: #858585;
    --brand-blue: #0c4d92;
    --brand-blue-light: #1462a6;
    --brand-blue-deep: #083f80;
    --ink-grey: #4a4b4d;
    --stripe-grey: #404246;
    --paper: #ffffff;
    --rule: rgba(255,255,255,0.55);
  }
  * { margin: 0; padding: 0; box-sizing: border-box; }
  html, body {
    width: 1200px; height: 1000px; overflow: hidden;
    background: var(--backdrop);
    font-family: "Source Sans 3", "Source Sans Pro", Arial, sans-serif;
  }
  .canvas { position: relative; width: 1200px; height: 1000px; }

  .card { position: absolute; overflow: hidden; }

  .card-front {
    left: 337px; top: 72px; width: 731px; height: 427px;
    background: radial-gradient(ellipse at 45% 80%, var(--brand-blue-light) 0%, var(--brand-blue) 55%, var(--brand-blue-deep) 100%);
  }
  .wordmark {
    position: absolute; display: flex; align-items: center; gap: 14px;
    font-weight: 700; letter-spacing: 1px; line-height: 1; white-space: nowrap;
  }
  .wordmark-dot { border-radius: 50%; flex: none; }
  .card-front .wordmark {
    left: 50%; top: 182px; transform: translateX(-50%);
    font-size: 84px; color: var(--paper);
  }
  .card-front .wordmark-dot { width: 34px; height: 34px; background: var(--paper); }

  .card-back {
    left: 97px; top: 518px; width: 726px; height: 425px;
    background: var(--paper);
  }
  .card-back .wordmark {
    left: 50%; top: 82px; transform: translateX(-50%);
    font-size: 78px; color: var(--ink-grey);
  }
  .card-back .wordmark-dot { width: 32px; height: 32px; background: var(--brand-blue); }

  .contact-band {
    position: absolute; left: 0; top: 214px; width: 100%; height: 211px;
    border-top: 8px solid var(--stripe-grey);
    background: radial-gradient(ellipse at 50% 60%, var(--brand-blue-light) 0%, var(--brand-blue) 60%, var(--brand-blue-deep) 100%);
    color: var(--paper);
  }
  .person { position: absolute; left: 147px; top: 72px; }
  .person-name { font-size: 24px; font-weight: 600; line-height: 1.2; }
  .person-title { font-size: 19px; font-weight: 400; margin-top: 2px; }

  .divider {
    position: absolute; left: 334px; top: 17px; width: 1px; height: 161px;
    background: var(--rule);
  }
  .details { position: absolute; left: 365px; top: 14px; font-size: 17px; }
  .address { line-height: 24px; }
  .contact-list { list-style: none; margin-top: 16px; }
  .contact-list li { display: flex; align-items: center; height: 26px; margin-bottom: 12px; }
  .contact-icon {
    width: 26px; height: 26px; border-radius: 3px; background: var(--paper);
    color: var(--brand-blue); font-weight: 700; font-size: 16px;
    display: flex; align-items: center; justify-content: center; margin-right: 22px;
  }
</style>
</head>
<body>
  <main class="canvas">
    <section class="card card-front" aria-label="Business card front">
      <div class="wordmark"><span class="wordmark-dot"></span><span>tarvulix</span></div>
    </section>

    <section class="card card-back" aria-label="Business card back">
      <div class="wordmark"><span class="wordmark-dot"></span><span>tarvulix</span></div>
      <div class="contact-band">
        <div class="person">
          <p class="person-name">Dana Whitlow</p>
          <p class="person-title">CEO</p>
        </div>
        <div class="divider"></div>
        <div class="details">
          <p class="address">4120 Harbor Lane, Suite 350<br>Marlow Bay, CA 90218</p>
          <ul class="contact-list">
            <li><span class="contact-icon">P</span>510-555-0148</li>
            <li><span class="contact-icon">E</span>info@tarvulix-hq.com</li>
            <li><span class="contact-icon">W</span>www.tarvulix-hq.com</li>
          </ul>
        </div>
      </div>
    </section>
  </main>
</body>
</html>
```